TovaLamarpe - Israeli Mental Health Website

We are developing an Israeli website for mental health. The website will be both in English and in Hebrew. We have a logo and would like a website design based on the logo and the logos colors (attached).

Attached is a doc that contains the website requirements.

We would like to have an icon for each of the sidebar categories, an image for each of the pages (including each of the sidebar category pages).

Target Market(s)

Adults 18-80

Industry/Entity Type

Mental Health

Number of Pages Required

5+ page

Font styles to use
Sans Serif

Colors

Designer to choose colors to be used in the design.

```html
<!DOCTYPE html>
<html lang="en">
<head>
<meta charset="utf-8">
<title>TovaLamarpe – Organization for Mental Health</title>
<link href="https://fonts.googleapis.com/css2?family=Poppins:wght@400;500;600;700&display=swap" rel="stylesheet">
<style>
:root{
  --blue:#2271c3;
  --blue-dark:#1c5fa8;
  --green:#4cae46;
  --green-dark:#3d9a3a;
  --ink:#2f2f2f;
  --body:#555;
  --muted:#8a8a8a;
  --sky:#e7f1fb;
  --sage:#e3eadf;
  --white:#fff;
}
*{box-sizing:border-box;margin:0;padding:0}
html,body{width:1200px;height:4552px;overflow:hidden}
body{position:relative;font-family:'Poppins',sans-serif;color:var(--ink);background:var(--white)}
.abs{position:absolute}
.btn{position:absolute;display:flex;align-items:center;justify-content:center;border-radius:30px;color:var(--white);font-weight:600;background:linear-gradient(180deg,var(--blue) 0%,var(--green) 100%);box-shadow:0 3px 6px rgba(0,0,0,.15)}
.chat-dot{position:absolute;border-radius:50%;background:var(--green);border:3px solid var(--white);box-shadow:0 0 0 2px var(--green)}
.para{font-size:15.5px;line-height:25.5px;color:var(--body)}
.title{font-weight:700;color:var(--ink)}

/* header */
.header{left:0;top:0;width:1200px;height:133px;background:var(--white)}
.brand{left:0;top:0;width:345px;height:133px;border-right:4px solid #eee;display:flex;align-items:center;justify-content:center;gap:10px;font-size:22px;font-weight:700;color:var(--blue)}
.brand .mark{width:26px;height:26px;border-radius:50%;background:var(--green)}
.lang{right:110px;top:18px;display:flex;align-items:center;gap:10px;font-size:22px;font-weight:600}
.lang .globe{width:34px;height:34px;border-radius:50%;background:var(--blue);border:3px solid var(--green)}
.nav a{position:absolute;top:84px;font-size:15px;font-weight:600;color:var(--ink);text-decoration:none}

/* sidebar */
.sidebar{left:0;top:133px;width:345px;height:557px;background:var(--blue)}
.sidebar li{list-style:none;height:41.3px;display:flex;align-items:center;padding-left:20px;gap:20px;color:var(--white);font-size:13.5px;font-weight:500;border-bottom:1px solid rgba(255,255,255,.18)}
.sidebar li.active{background:var(--green)}
.sidebar svg{width:22px;height:22px;flex:none;fill:none;stroke:var(--white);stroke-width:2;stroke-linecap:round;stroke-linejoin:round}
.hero{left:345px;top:133px;width:855px;height:557px;background:
  radial-gradient(ellipse 230px 280px at 55% 55%,#4a4540 0%,rgba(74,69,64,0) 100%),
  radial-gradient(ellipse 260px 200px at 82% 62%,#b9b5b1 0%,rgba(185,181,177,0) 100%),
  linear-gradient(90deg,#f2f1ee 0%,#d9d6d1 35%,#9b9893 75%,#6f6c68 100%)}

/* emergency */
.em-photo{left:100px;top:777px;width:378px;height:368px;border-radius:50%;border-left:9px solid var(--green);background:
  radial-gradient(ellipse 120px 130px at 55% 40%,#3c4d63 0%,rgba(60,77,99,0) 100%),
  radial-gradient(ellipse 180px 150px at 65% 78%,#2f5c92 0%,rgba(47,92,146,0) 100%),
  linear-gradient(135deg,#eef0f2 0%,#c9d2da 45%,#6d8fb8 100%)}

/* chat band */
.band{left:0;top:1280px;width:1200px;height:453px;background:var(--green)}
.band-dot{left:24px;top:1405px;width:200px;height:200px;border-radius:50%;background:var(--green-dark);border:5px solid var(--white)}
.band h2{position:absolute;left:0;width:1200px;top:1370px;text-align:center;font-size:36px;color:var(--white)}
.band p{position:absolute;left:245px;width:710px;top:1430px;text-align:center;color:var(--white);font-size:15.5px;line-height:26px}

/* therapists */
.therapists{left:0;top:1733px;width:1200px;height:754px;background:var(--sky)}
.card{position:absolute;top:1957px;width:277px;height:363px;background:var(--white);box-shadow:0 2px 8px rgba(0,0,0,.08)}
.card .face{position:absolute;left:50px;top:30px;width:176px;height:176px;border-radius:50%;background:
  radial-gradient(ellipse 60px 80px at 50% 75%,#f4f6f8 0%,rgba(244,246,248,0) 100%),
  linear-gradient(180deg,var(--blue) 0%,#2a8f7e 55%,var(--green) 100%)}
.card .name{position:absolute;top:243px;width:100%;text-align:center;font-weight:600;font-size:16px}
.card .role{position:absolute;top:272px;width:100%;text-align:center;font-size:14px;color:var(--muted)}

/* orgs */
.org-frame{left:667px;top:2594px;width:133px;height:205px;background:var(--green)}
.org-photo{left:701px;top:2626px;width:416px;height:411px;background:
  radial-gradient(ellipse 140px 190px at 48% 55%,#5d6b68 0%,rgba(93,107,104,0) 100%),
  radial-gradient(ellipse 200px 160px at 15% 10%,#fff4dc 0%,rgba(255,244,220,0) 100%),
  linear-gradient(135deg,#f0dcbd 0%,#b8977a 45%,#77767d 100%)}

/* videos */
.videos{left:0;top:3178px;width:1200px;height:900px;background:var(--sage)}
.video{left:222px;top:3538px;width:756px;height:393px;background:
  radial-gradient(ellipse 170px 180px at 70% 55%,#4b4f5a 0%,rgba(75,79,90,0) 100%),
  radial-gradient(ellipse 160px 200px at 12% 60%,#e8eee6 0%,rgba(232,238,230,0) 100%),
  linear-gradient(120deg,#c9d3c9 0%,#9fb0bd 50%,#3f74bf 100%)}
.play{left:548px;top:3685px;width:104px;height:104px;border-radius:50%;background:#1d1d1d;border:6px solid var(--white);box-shadow:0 0 0 4px #1d1d1d}
.play:after{content:"";position:absolute;left:36px;top:26px;border-left:34px solid var(--white);border-top:20px solid transparent;border-bottom:20px solid transparent}

/* footer */
.footer-base{left:0;top:4078px;width:1200px;height:474px;background:var(--blue)}
.footer-brand{left:0;width:1200px;top:4210px;display:flex;flex-direction:column;align-items:center;gap:18px;color:var(--white);font-size:44px;font-weight:700}
.footer-brand .mark{width:70px;height:70px;border-radius:50%;background:var(--white)}
.legal{top:4490px;font-size:14px;color:var(--white)}
.legal.link{text-decoration:underline}
</style>
</head>
<body>

<header class="abs header"></header>
<div class="abs brand"><span class="mark"></span>TovaLamarpe</div>
<div class="abs lang"><span class="globe"></span>English ▾</div>
<nav class="nav">
  <a style="left:467px">Therapists</a>
  <a style="left:577px">Organizations</a>
  <a style="left:715px">Videos</a>
  <a style="left:815px">Contact</a>
  <a style="left:909px">About</a>
  <a style="left:986px">Donate</a>
</nav>

<ul class="abs sidebar">
  <li class="active"><svg viewBox="0 0 24 24"><path d="M5 3h4l2 5-2.5 1.5a11 11 0 0 0 6 6L16 13l5 2v4a2 2 0 0 1-2 2A16 16 0 0 1 3 5a2 2 0 0 1 2-2z"/></svg>Emergency Mental Help</li>
  <li><svg viewBox="0 0 24 24"><circle cx="12" cy="4" r="2.5"/><path d="M12 7v14M8 11h8M9 21h6"/></svg>Suicide</li>
  <li><svg viewBox="0 0 24 24"><path d="M12 2l8 3v6c0 5-3.5 9-8 11-4.5-2-8-6-8-11V5z"/><path d="M9 12l2 2 4-4"/></svg>Sexual Assault/Violence Victims</li>
  <li><svg viewBox="0 0 24 24"><path d="M3 9h14v6H3zM17 11h4M7 9V6M11 9V6"/></svg>Sexual Assault/Violence Assaulters</li>
  <li><svg viewBox="0 0 24 24"><path d="M13 2L5 13h6l-1 9 8-11h-6z"/></svg>Post Trauma</li>
  <li><svg viewBox="0 0 24 24"><path d="M7 15a4 4 0 0 1 0-8 5 5 0 0 1 9.5 1A3.5 3.5 0 0 1 17 15z"/><path d="M8 18v3M12 18v3M16 18v3"/></svg>Depression</li>
  <li><svg viewBox="0 0 24 24"><path d="M3 12h4l2-5 4 10 2-5h6"/></svg>Anxiety</li>
  <li><svg viewBox="0 0 24 24"><path d="M10 2h4v4l2 3v13H8V9l2-3z"/><path d="M8 14h8"/></svg>Addictions</li>
  <li><svg viewBox="0 0 24 24"><path d="M20 14A8 8 0 1 1 10 4a6 6 0 0 0 10 10z"/></svg>Sleep Disorders</li>
  <li><svg viewBox="0 0 24 24"><path d="M7 2v20M4 2v6a3 3 0 0 0 6 0V2M17 22V2c-3 2-3 8 0 10"/></svg>Eating Disorders</li>
  <li><svg viewBox="0 0 24 24"><circle cx="12" cy="12" r="9"/><path d="M15 9h-4a1.5 1.5 0 0 0 0 3h2a1.5 1.5 0 0 1 0 3H9M12 6v2M12 16v2"/></svg>Financial Problems</li>
  <li><svg viewBox="0 0 24 24"><circle cx="7" cy="5" r="2.5"/><circle cx="17" cy="9" r="2"/><path d="M7 9v12M4 12h6M17 12v9M14.5 15h5"/></svg>Parenthood</li>
  <li><svg viewBox="0 0 24 24"><path d="M8 19S2 15 2 10a3.5 3.5 0 0 1 6-2.5A3.5 3.5 0 0 1 14 10c0 5-6 9-6 9z"/><path d="M16 7.5A3.5 3.5 0 0 1 22 10c0 5-6 9-6 9"/></svg>Relationship</li>
</ul>
<div class="abs hero" role="img" aria-label="Photo of a young woman wearing a face mask sitting thoughtfully on a sofa"></div>
<div class="chat-dot" style="left:1132px;top:262px;width:40px;height:40px"></div>

<!-- Emergency -->
<div class="abs em-photo" role="img" aria-label="Photo of a distressed man holding his head in his hands"></div>
<h2 class="abs title" style="left:523px;top:800px;font-size:36px">Emergency Mental Help</h2>
<p class="abs para" style="left:527px;top:860px;width:530px">Lorem ipsum dolor sit amet, consectetur adipiscing elit, sed do eiusmod tempor incididunt ut labore et dolore magna aliqua. Ut enim ad minim veniam, quis nostrud exercitation ullamco laboris nisi ut aliquip ex ea commodo consequat. Duis aute irure dolor in reprehenderit in voluptate velit esse cillum dolore eu fugiat nulla pariatur. Excepteur sint occaecat cupidatat non proident, sunt in culpa qui officia deserunt mollit anim id est laborum.</p>
<div class="btn" style="left:519px;top:1085px;width:390px;height:58px;font-size:15.5px;font-weight:500">More options for Emergency Mental Help</div>

<!-- Chat band -->
<section class="abs band"></section>
<div class="abs band-dot"></div>
<section class="band" style="background:none">
  <h2>Smart QuickChat</h2>
  <p>Lorem ipsum dolor sit amet, consectetur adipiscing elit, sed do eiusmod tempor incididunt ut labore et dolore magna aliqua. Ut enim ad minim veniam, quis nostrud exercitation ullamco laboris nisi ut aliquip ex ea commodo consequat. Duis aute irure dolor in reprehenderit in voluptate velit esse cillum dolore eu fugiat</p>
</section>
<div class="btn" style="left:458px;top:1570px;width:283px;height:58px;font-size:22px;font-weight:700;letter-spacing:1px">XXXX7 878 X788</div>

<!-- Therapists -->
<section class="abs therapists"></section>
<h2 class="abs title" style="left:0;width:1200px;text-align:center;top:1792px;font-size:36px">Therapists</h2>
<p class="abs para" style="left:245px;width:710px;top:1850px;text-align:center">Lorem ipsum dolor sit amet, consectetur adipiscing elit, sed do eiusmod tempor incididunt ut labore et dolore magna aliqua. Ut enim ad minim veniam, quis nostrud exercitation ullamco laboris nisi ut aliquip ex ea commodo consequat.</p>
<div class="card" style="left:147px"><div class="face" role="img" aria-label="Portrait photo of a therapist"></div><div class="name">Therapist name</div><div class="role">Lorem Ipsum</div><div class="chat-dot" style="left:32px;top:313px;width:28px;height:28px"></div></div>
<div class="card" style="left:461px"><div class="face" role="img" aria-label="Portrait photo of a therapist"></div><div class="name">Therapist name</div><div class="role">Lorem Ipsum</div><div class="chat-dot" style="left:32px;top:313px;width:28px;height:28px"></div></div>
<div class="card" style="left:776px"><div class="face" role="img" aria-label="Portrait photo of a therapist"></div><div class="name">Therapist name</div><div class="role">Lorem Ipsum</div><div class="chat-dot" style="left:32px;top:313px;width:28px;height:28px"></div></div>
<div class="btn" style="left:458px;top:2358px;width:283px;height:60px;font-size:15px">FIND THERAPISTS</div>

<!-- Organizations -->
<h2 class="abs title" style="left:147px;top:2670px;font-size:36px">Organizations</h2>
<p class="abs para" style="left:150px;top:2738px;width:490px">Lorem ipsum dolor sit amet, consectetur adipiscing elit, sed do eiusmod tempor incididunt ut labore et dolore magna aliqua. Ut enim ad minim veniam, quis nostrud exercitation ullamco laboris nisi ut aliquip ex ea commodo consequat. Duis aute irure dolor in reprehenderit in voluptate velit esse cillum dolore eu fugiat nulla pariatur. Excepteur sint occaecat cupidatat non proident, sunt in culpa qui officia deserunt mollit anim id est laborum.</p>
<div class="btn" style="left:150px;top:2966px;width:245px;height:60px;font-size:15px">FIND ORGANIZATIONS</div>
<div class="abs org-frame"></div>
<div class="abs" style="left:701px;top:2626px;width:99px;height:173px;background:var(--white)"></div>
<div class="abs org-photo" role="img" aria-label="Photo of two women embracing at a support group meeting"></div>

<!-- Videos -->
<section class="abs videos"></section>
<h2 class="abs title" style="left:0;width:1200px;text-align:center;top:3262px;font-size:36px">Videos</h2>
<p class="abs para" style="left:240px;width:720px;top:3330px;text-align:center">Lorem ipsum dolor sit amet, consectetur adipiscing elit, sed do eiusmod tempor ut labore et dolore magna aliqua. Ut enim ad minim veniam, quis nostrud exercitation ullamco laboris nisi ut aliquip ex ea commodo consequats aute irure dolo.</p>
<div class="btn" style="left:477px;top:3440px;width:246px;height:58px;font-size:15px">VIDEO LIBRARY</div>

<!-- Footer -->
<div class="abs footer-base"></div>
<svg class="abs" style="left:0;top:3860px" width="1200" height="692" viewBox="0 0 1200 692">
  <path d="M0 0 C120 90 300 240 560 240 C800 240 980 150 1200 118 L1200 692 L0 692 Z" fill="#4cae46"/>
  <path d="M0 118 C220 200 420 262 620 262 C840 262 1010 170 1200 132 L1200 692 L0 692 Z" fill="#2271c3"/>
</svg>
<div class="abs video" role="img" aria-label="Video still of a therapist in session with a young man on a sofa"></div>
<div class="abs play"></div>

<div class="chat-dot" style="left:52px;top:4170px;width:40px;height:40px"></div>
<div class="abs footer-brand"><span class="mark"></span>TovaLamarpe</div>
<div class="abs legal" style="left:152px">TovaLamarpe - Organization for Mental Health ©2023</div>
<div class="abs legal link" style="left:818px">Privacy Policy</div>
<div class="abs legal link" style="left:1000px">Terms</div>

</body>
</html>
```